Card Show Flyer- for use on instagram, facebook and twitter

My usual digital flyer designer isnt getting back to me. I need something that looks like the image that I am uploading with a new design for our next show.
Dellmoor Trading Jamboree-Memorial Day Show
742 N. Halvard Lane
Corvalle Indiana 47812
Monday, May 29th-Show- 8:30-3:30
Sunday, May 28th-Trade Night- 6pm-10pm
180+ Sold Out Tables
Notes
-use trade night sponsored by Gripline Kiosks
-use pavrin top banner like the copy i am submitting
-use tumbleweed logo at bottom with "Best Kids Card Scavenger Hunt in the Midwest"
-use QVR logo with "official group grading submitter for Dellmoor Trading Jamboree"
Attaching our Orlo Athletics logo as well for your use where needed
Thanks! Gary Tolliver

Target Market(s)

Collectors, Attendance for card show

Industry/Entity Type

Collectibles/Trade Show

Requirements
Must have
• My logo and specifics for partnerships

```html
<!DOCTYPE html>
<html lang="en">
<head>
<meta charset="utf-8">
<title>Dellmoor Trading Jamboree – Memorial Day Show</title>
<link rel="stylesheet" href="https://fonts.googleapis.com/css2?family=Archivo+Black&family=Roboto+Condensed:wght@300;400;700&display=swap">
<style>
  :root{
    --navy:#1b1e29;
    --navy-deep:#12141c;
    --yellow:#ffd800;
    --amber:#f5a313;
    --blue:#2f6fbb;
    --white:#ffffff;
    --red:#d9231a;
    --bulb:#ffcf5a;
    --grey:#5b5b5b;
    --ink:#111111;
  }
  *{margin:0;padding:0;box-sizing:border-box}
  html,body{width:927px;height:1200px;overflow:hidden;background:var(--navy)}
  .flyer{
    position:relative;width:927px;height:1200px;overflow:hidden;
    background:radial-gradient(ellipse at 30% 25%, #2a2e3c 0%, var(--navy) 55%, var(--navy-deep) 100%);
    font-family:"Roboto Condensed", "Arial Narrow", sans-serif;color:var(--white);
  }
  .honey-band{
    position:absolute;left:0;top:516px;width:927px;height:134px;
    background:linear-gradient(180deg,var(--amber) 0%,var(--yellow) 40%,var(--yellow) 65%,var(--amber) 100%);
  }
  .headline{position:absolute;left:0;top:0;width:927px;height:520px}
  .title-top{font-family:"Archivo Black",sans-serif;fill:var(--yellow)}
  .title-main{font-family:"Archivo Black",sans-serif;fill:var(--blue)}
  .occasion{font-family:"Roboto Condensed",sans-serif;font-weight:700;fill:var(--white);stroke:var(--blue);stroke-width:3;paint-order:stroke}
  .marquee{font-family:"Archivo Black",sans-serif;fill:var(--red);stroke:var(--bulb);stroke-width:4;paint-order:stroke}

  .club-badge{
    position:absolute;left:551px;top:263px;width:374px;height:374px;border-radius:50%;
    background:var(--blue);display:flex;align-items:center;justify-content:center;text-align:center;
    font-family:"Archivo Black",sans-serif;font-size:38px;line-height:1.1;color:var(--white);
  }

  .venue-card{
    position:absolute;left:59px;top:534px;width:490px;height:221px;
    background:var(--white);border-radius:10px;padding:11px;
  }
  .venue-photo{
    width:468px;height:142px;
    background:linear-gradient(180deg,#c9d4de 0%,#b8becb 28%,#a8322d 30%,#8f2622 70%,#5f8a3e 78%,#7aa052 100%);
  }
  .venue-address{
    height:55px;background:var(--ink);display:flex;align-items:center;justify-content:center;
    font-weight:700;font-size:19px;letter-spacing:.1px;
  }

  .tables{position:absolute;left:91px;top:781px;font-family:"Archivo Black",sans-serif;font-size:29px;color:var(--blue);letter-spacing:.5px}

  .day{font-weight:700;line-height:1;position:absolute}
  .day-name{color:var(--yellow);display:block}
  .day-name .comma{color:var(--white)}
  .day-detail{display:block;color:var(--white)}
  .day-detail sup{font-size:.55em;vertical-align:.7em}

  .sunday{left:86px;top:830px}
  .sunday .day-name{font-size:84px}
  .sunday .day-detail{font-size:50px;margin-top:12px}
  .sunday .day-detail + .day-detail{margin-top:10px}

  .monday{left:584px;top:694px}
  .monday .day-name{font-size:80px}
  .monday .day-detail{font-size:46px;margin-top:8px}
  .monday .day-detail + .day-detail{font-size:40px;margin-top:10px}

  .sponsor-heading{position:absolute;left:690px;top:890px;width:190px;text-align:right;font-weight:700;line-height:.86}
  .sponsor-heading .trade{display:block;color:var(--blue);font-size:66px}
  .sponsor-heading .night{display:block;color:var(--white);font-size:66px}
  .sponsor-heading .by{display:block;font-weight:300;font-size:31px;margin-top:8px;line-height:1;text-align:center;padding-left:14px}

  .partners{position:absolute;left:0;top:1057px;width:927px;height:104px}
  .partner-mark{position:absolute;top:0;height:104px;display:flex;align-items:center;justify-content:center;font-family:"Roboto Condensed",sans-serif;font-weight:700;text-align:center}
  .mark-tumbleweed{left:82px;width:112px;background:var(--grey);color:var(--white);font-size:17px}
  .mark-qvr{left:357px;width:99px;background:var(--white);color:var(--blue);font-size:32px}
  .mark-gripline{left:689px;width:184px;background:var(--white);color:var(--ink);font-size:24px}
  .partner-note{position:absolute;top:2px;font-weight:300;font-size:20px;line-height:1.25;color:var(--white)}
  .note-tumbleweed{left:207px;width:130px}
  .note-qvr{left:482px;width:160px}
</style>
</head>
<body>
<main class="flyer">
  <div class="honey-band"></div>

  <svg class="headline" viewBox="0 0 927 520" aria-label="Dellmoor Trading Jamboree Memorial Day Show">
    <text class="title-top" x="55" y="131" font-size="92" textLength="738" lengthAdjust="spacingAndGlyphs">DELLMOOR</text>
    <text class="title-main" x="55" y="243" font-size="122" textLength="738" lengthAdjust="spacingAndGlyphs">TRADING JAMBOREE</text>
    <text class="occasion" x="69" y="328" font-size="80" textLength="502" lengthAdjust="spacingAndGlyphs">MEMORIAL DAY</text>
    <text class="marquee" x="62" y="498" font-size="190" textLength="440" lengthAdjust="spacingAndGlyphs">SHOW</text>
  </svg>

  <div class="club-badge">DELLMOOR<br>TRADING<br>JAMBOREE</div>

  <section class="venue-card">
    <div class="venue-photo" role="img" aria-label="Photo of the red barn-style venue building with green lawn and trees"></div>
    <div class="venue-address">742 N. Halvard Lane Corvalle Indiana 47812</div>
  </section>

  <p class="tables">180+ SOLD OUT TABLES</p>

  <div class="day monday">
    <span class="day-name">MONDAY<span class="comma">,</span></span>
    <span class="day-detail">MAY 29<sup>TH</sup> SHOW</span>
    <span class="day-detail">8:30-3:30</span>
  </div>

  <div class="day sunday">
    <span class="day-name">SUNDAY<span class="comma">,</span></span>
    <span class="day-detail">MAY 28<sup>TH</sup> TRADE NIGHT</span>
    <span class="day-detail">6PM-10PM</span>
  </div>

  <div class="sponsor-heading">
    <span class="trade">TRADE</span>
    <span class="night">NIGHT</span>
    <span class="by">sponsored by</span>
  </div>

  <section class="partners">
    <div class="partner-mark mark-tumbleweed">TUMBLEWEED</div>
    <p class="partner-note note-tumbleweed">Best Kids Card Scavenger Hunt in the Midwest</p>
    <div class="partner-mark mark-qvr">QVR</div>
    <p class="partner-note note-qvr">Official group grading submitter for Dellmoor Trading Jamboree</p>
    <div class="partner-mark mark-gripline">Gripline Kiosks</div>
  </section>
</main>
</body>
</html>
```